Brintell's Business Card

I need some designs for a new business card including the new logo attached. An old example of our business card is also attached to show all the data that should be included on the new design.
**I added some more examples someone had mocked up**

Contact Information for Business Card

Should include all info on other examples uploaded.

```html
<!DOCTYPE html>
<html lang="en">
<head>
<meta charset="utf-8">
<title>Brintell's Business Card</title>
<link rel="stylesheet" href="https://fonts.googleapis.com/css2?family=Montserrat:wght@400;500;600;700;800&display=swap">
<style>
  :root {
    --backdrop: #3a3a3a;
    --brand-blue: #1b2a9c;
    --logo-blue: #1f6fd1;
    --brand-red: #e8202a;
    --white: #ffffff;
  }
  * { box-sizing: border-box; margin: 0; padding: 0; }
  html, body {
    width: 1200px; height: 910px; overflow: hidden;
    background: var(--backdrop);
    font-family: "Montserrat", sans-serif;
  }
  .sheet {
    position: relative; width: 1200px; height: 910px;
    display: flex; align-items: center; justify-content: center; gap: 50px;
  }
  .card {
    position: relative; width: 525px; height: 300px;
    border-radius: 22px; overflow: hidden;
    background: var(--brand-blue); color: var(--white);
  }
  /* front */
  .card-front .accent-tick {
    position: absolute; left: 0; top: 22px; width: 5px; height: 30px;
    background: var(--brand-red);
  }
  .card-front .white-panel { position: absolute; inset: 0; }
  .contact { position: absolute; left: 34px; top: 30px; }
  .contact .person { font-size: 26px; font-weight: 800; letter-spacing: .3px; margin-bottom: 14px; }
  .contact .line { display: flex; align-items: center; gap: 8px; font-size: 15px; font-weight: 500; margin-bottom: 6px; }
  .contact svg { width: 13px; height: 13px; fill: var(--white); flex: none; }
  .credentials {
    position: absolute; left: 34px; bottom: 72px;
    font-size: 11px; font-weight: 500; line-height: 1.35; text-transform: uppercase;
  }
  .front-logo { position: absolute; right: 28px; bottom: 78px; }
  .wordmark { display: flex; align-items: center; gap: 8px; font-weight: 700; line-height: 1; }
  .wordmark .dot { width: 13px; height: 13px; border-radius: 50%; background: var(--brand-red); flex: none; }
  .front-logo .wordmark { font-size: 32px; color: var(--logo-blue); }
  .tagline { font-size: 9px; font-weight: 600; color: var(--brand-red); text-transform: uppercase; margin-top: 5px; letter-spacing: .3px; }
  /* back */
  .service-area {
    position: absolute; left: 34px; top: 40px;
    font-size: 14px; font-weight: 400; line-height: 1.25;
  }
  .back-logo { position: absolute; left: 205px; top: 92px; }
  .back-logo .wordmark { font-size: 44px; color: var(--white); }
  .back-logo .tagline { font-size: 9.5px; }
  .call-out {
    position: absolute; left: 205px; bottom: 48px;
    font-size: 14px; font-weight: 500; line-height: 1.2; text-transform: uppercase;
  }
</style>
</head>
<body>
<main class="sheet">
  <section class="card card-front" aria-label="Business card front">
    <svg class="white-panel" viewBox="0 0 525 300" preserveAspectRatio="none" aria-hidden="true">
      <path d="M235 300 C 212 225, 232 150, 310 140 C 400 128, 445 78, 525 68 L 525 300 Z" fill="var(--white)"/>
      <path d="M235 300 C 212 225, 232 150, 310 140 C 400 128, 445 78, 525 68" fill="none" stroke="var(--brand-red)" stroke-width="7"/>
    </svg>
    <span class="accent-tick"></span>
    <div class="contact">
      <h1 class="person">Dale Brintell</h1>
      <p class="line">
        <svg viewBox="0 0 24 24" aria-hidden="true"><path d="M6.6 10.8a15.1 15.1 0 0 0 6.6 6.6l2.2-2.2a1 1 0 0 1 1-.25 11.4 11.4 0 0 0 3.6.57 1 1 0 0 1 1 1V20a1 1 0 0 1-1 1A17 17 0 0 1 3 4a1 1 0 0 1 1-1h3.5a1 1 0 0 1 1 1c0 1.25.2 2.45.57 3.57a1 1 0 0 1-.25 1z"/></svg>
        555.014.2290
      </p>
      <p class="line">
        <svg viewBox="0 0 24 24" aria-hidden="true"><path d="M2 5h20v14H2z M2 5l10 8 10-8" /></svg>
        brintellhvac@mail.com
      </p>
    </div>
    <p class="credentials">Licensed &amp; Insured<br>Family Owned &amp; Operated</p>
    <div class="front-logo">
      <div class="wordmark"><span class="dot"></span>BRINTELL'S</div>
      <p class="tagline">Air Conditioning &amp; Heating Service</p>
    </div>
  </section>

  <section class="card card-back" aria-label="Business card back">
    <p class="service-area">Serves Maple Ridge,<br>IA &amp; Surrounding Areas</p>
    <div class="back-logo">
      <div class="wordmark"><span class="dot"></span>BRINTELL'S</div>
      <p class="tagline">Air Conditioning &amp; Heating Service</p>
    </div>
    <p class="call-out">Call today for<br>all your HVAC, refrigeration<br>&amp; plumbing needs</p>
  </section>
</main>
</body>
</html>
```